Cobbleford Works New Website

Custom Wood Cabinetry and Precisions Wood Cutting website. I have created a pdf document with all the specs for the project and attached it. I am just typing stuff in here so it stops telling me my description is too short. Their once was a man from Nantucket.. he used to pee in a bucket.. roses are red, cardinals are birds, i wish they didn't require 300 words.
Number of Pages Required
1 page

```html
<!DOCTYPE html>
<html lang="en">
<head>
<meta charset="utf-8">
<title>Cobbleford Works</title>
<link href="https://fonts.googleapis.com/css2?family=Barlow:wght@500;600;700&family=Open+Sans:wght@400;600&display=swap" rel="stylesheet">
<style>
:root{
  --brown-dark:#5a2e17;
  --brown-deep:#3a1c0e;
  --accent:#d9875a;
  --accent-line:#d99a72;
  --text:#4a4a4a;
  --white:#ffffff;
  --frame:#8a5a44;
}
*{box-sizing:border-box;margin:0;padding:0}
html,body{width:1108px;height:1200px;overflow:hidden;background:var(--white)}
body{font-family:"Open Sans",sans-serif;color:var(--text)}
.page{width:1108px;height:1200px;overflow:hidden;position:relative}

.site-header{height:88px;display:flex;align-items:center;padding:0 50px;gap:40px}
.brand{display:flex;align-items:center;gap:10px;width:160px;font-family:"Barlow",sans-serif;font-weight:700;font-size:20px;color:var(--brown-dark);line-height:1.05}
.brand-dot{width:12px;height:12px;border-radius:50%;background:var(--brown-dark);flex:none}
.search{display:flex;width:422px;height:32px;border:1px solid var(--brown-dark)}
.search input{flex:1;border:0;padding:0 10px;font:11px "Open Sans",sans-serif;color:#666}
.search button{width:32px;border:0;background:var(--brown-deep);display:flex;align-items:center;justify-content:center}
.cart{margin-left:60px;display:flex;align-items:center;gap:4px;font-size:11px;color:#333}
.cart-icon{position:relative}
.cart-badge{position:absolute;top:-6px;right:-6px;width:11px;height:11px;border-radius:50%;background:#d3232a;color:#fff;font-size:7px;text-align:center;line-height:11px}
.call{margin-left:auto;display:flex;gap:16px;align-items:flex-start;font-size:12px;color:#333}
.call small{display:block;font-size:10px;color:#666}

.main-nav{height:54px;background:var(--brown-dark);display:flex;align-items:center;padding-left:54px;gap:54px}
.main-nav a{font-family:"Barlow",sans-serif;font-weight:600;font-size:15px;color:var(--white);text-decoration:none}
.main-nav a.active{color:var(--accent)}

.hero{position:relative;height:534px;background:linear-gradient(160deg,#8a5a34 0%,#6e4322 35%,#5a3518 65%,#3f230f 100%)}
.hero-title{position:absolute;left:85px;top:170px;font-family:"Barlow",sans-serif;font-weight:600;font-size:42px;line-height:1.26;color:var(--white)}
.btn-read{position:absolute;left:85px;top:428px;width:210px;height:42px;border-radius:21px;background:var(--accent);color:#fff;font-size:16px;display:flex;align-items:center;justify-content:center}
.hero-arrow{position:absolute;top:248px}
.hero-arrow.left{left:22px}.hero-arrow.right{right:22px}
.dots{position:absolute;left:468px;top:497px;display:flex;gap:9px}
.dots span{width:11px;height:11px;border-radius:50%;background:rgba(255,255,255,.45)}
.dots span:first-child{background:#fff}

.about{display:flex;padding:56px 104px 0 100px;justify-content:space-between}
.about-text{width:510px;padding-top:30px}
.section-kicker{font-family:"Barlow",sans-serif;font-weight:600;font-size:24px;color:var(--brown-dark);padding-bottom:10px;border-bottom:1px solid var(--accent-line)}
.about-text p{font-size:14px;line-height:1.75;margin-top:22px;color:#555}
.about-text p+p{margin-top:18px}
.framed{width:330px;height:248px;border:1px solid var(--frame);padding:8px}
.framed div{width:100%;height:100%;background:linear-gradient(135deg,#6b3c1c,#b27a45 55%,#e6ded4)}

.creations{padding:100px 48px 0 50px}
.section-title{font-family:"Barlow",sans-serif;font-weight:600;font-size:36px;color:var(--brown-dark);width:496px;padding-bottom:8px;border-bottom:1.5px solid var(--accent-line)}
.browse{text-align:right;font-size:15px;color:#444;margin-top:14px;padding-right:8px}
.products{display:flex;gap:18px;margin-top:40px}
.product{width:238px;height:242px}
</style>
</head>
<body>
<div class="page">
  <header class="site-header">
    <div class="brand"><span class="brand-dot"></span>Cobbleford Works</div>
    <div class="search">
      <input type="text" value="What can we help you find?" aria-label="Search">
      <button aria-label="Search"><svg width="13" height="13" viewBox="0 0 14 14"><circle cx="6" cy="6" r="4.2" fill="none" stroke="#fff" stroke-width="1.8"/><line x1="9" y1="9" x2="13" y2="13" stroke="#fff" stroke-width="1.8"/></svg></button>
    </div>
    <div class="cart">$0.00
      <span class="cart-icon"><svg width="18" height="16" viewBox="0 0 18 16"><path d="M1 2h3l2 9h9l2-7H5" fill="none" stroke="#333" stroke-width="1.4"/><circle cx="7" cy="14" r="1.3" fill="#333"/><circle cx="14" cy="14" r="1.3" fill="#333"/></svg><span class="cart-badge">0</span></span>
    </div>
    <div class="call">
      <svg width="18" height="18" viewBox="0 0 20 20"><path d="M4 2l3 0 1.5 4-2 1.5c1 2.3 2.7 4 5 5l1.5-2 4 1.5v3c0 1-1 2-2 2C9 17 3 11 2 4c0-1 1-2 2-2z" fill="none" stroke="#444" stroke-width="1.2"/></svg>
      <div>1-555-300-7788<small>Call us</small></div>
    </div>
  </header>

  <nav class="main-nav">
    <a class="active" href="#">Home</a><a href="#">About</a><a href="#">FAQs</a><a href="#">Contact</a><a href="#">Services ⌄</a>
  </nav>

  <section class="hero" role="img" aria-label="Photo of a knotty alder wood kitchen with custom cabinets seen through a brick archway">
    <h1 class="hero-title">Custom Cabinetry,<br>Precision Wood Cutting and<br>Custom Wood Art Company</h1>
    <div class="btn-read">Read more</div>
    <svg class="hero-arrow left" width="16" height="30" viewBox="0 0 16 30"><polyline points="14,2 2,15 14,28" fill="none" stroke="rgba(255,255,255,.7)" stroke-width="2"/></svg>
    <svg class="hero-arrow right" width="16" height="30" viewBox="0 0 16 30"><polyline points="2,2 14,15 2,28" fill="none" stroke="rgba(255,255,255,.7)" stroke-width="2"/></svg>
    <div class="dots"><span></span><span></span><span></span><span></span></div>
  </section>

  <section class="about">
    <div class="about-text">
      <h2 class="section-kicker">15 YEARS OF WOODWORKER</h2>
      <p>Since our beginning in 1999, we have worked tirelessly to earn our reputation for quality, service and dependability.</p>
      <p>For over 15 years these founding priciples have helped us succeed in creating prestigious architectural woodwork projects on a global scale. Our expert staffs provides a superior level of service.</p>
    </div>
    <div class="framed"><div role="img" aria-label="Close-up photo of built-in wooden shelving with a ladder rail"></div></div>
  </section>

  <section class="creations">
    <h2 class="section-title">Newest Creations</h2>
    <div class="browse">Browse All Items &gt;</div>
    <div class="products">
      <div class="product" role="img" aria-label="Carved wooden flag with eagle" style="background:linear-gradient(135deg,#b9b2a8,#7d766c)"></div>
      <div class="product" role="img" aria-label="Carved family name sign with pine trees and deer" style="background:linear-gradient(135deg,#c4b6a0,#6f5e48)"></div>
      <div class="product" role="img" aria-label="Engraved dark wood name sign" style="background:linear-gradient(135deg,#6b4a33,#3d2817)"></div>
      <div class="product" role="img" aria-label="Wooden wedding plaque with rope cross" style="background:linear-gradient(135deg,#c49a62,#8a6232)"></div>
    </div>
  </section>
</div>
</body>
</html>
```